Full Service Day Spa Needs Wordpress Template Designed

Verdant Spa is a full service day spa, where we make our own line of bath and body products. The current website houses an online store with an TradeNook base (as a WordPress plugin) and simple web pages with information and price lists for services.
For the upgraded website, we are doing a significant makeover and want to include the ability to have full screen video on our main page, windowed or full screen video on feature pages (for example, pages for "Meet our staff" or "Product Demos")
The site should retain standard WordPress compatibility for plugins, such as galleries etc.
The ability to include iframes would be considered a plus so that we can embed external scheduling applications that we subscribe to.
The color scheme for our spa features chocolate brown, taupe, cream, and turquoise for color accents. We would like our website to reflect these colors as our customers find them relaxing.
Our spa has a number of paintings on our walls, which could be used for inspiration for the website design. We like modern abstract art, with curves and swirls. I have included examples of this artwork so that potential designers can see what we like.
The new site must include our logo (provided) and our tag line: "Come Relax With Us" displayed in the upper left in the header.
We would prefer to have the option to put the menu either on the left side, or across the top to the right of the logo.
Words to describe the look we are seeking would be elegant, upscale, relaxing.

Target Market(s)

Our market is primarily local women (in and around our city) who are professionals aged 30 - 65.

Industry/Entity Type

Store

Colors
f78f20
00a990
f37022

Requirements
Must have
• The template should accommodate full screen and partial screen HTML5 video. Must have a menu, could be top or could be side. Should be in shades of browns and neutral colors, with teal accents, or similar highlights to the attached pictures of our artwork we have in the spa. We are looking for a consistent look that our customers can identify is us. Must have our logo in the upper left side of the header.
Nice to have
• Iframes built in would be nice, although we know we can get plugins for that. Likewise we know we can get plugins for the HTML 5 video, we would like the template built with accommodating that in mind. We have seen sites that have full screen video on the main page. We think this looks good.
Should not have
• We are looking for something elegant and upscale, so we are not looking for something "Cartoonish".

```html
<!DOCTYPE html>
<html lang="en">
<head>
<meta charset="utf-8">
<title>Verdant Spa</title>
<link rel="stylesheet" href="https://fonts.googleapis.com/css2?family=Questrial&family=Arimo:wght@400;700&display=swap">
<style>
:root{
  --teal:#5cc3be;
  --teal-dark:#3fb0aa;
  --brown-dark:#241913;
  --brown:#4a3126;
  --taupe:#a8896c;
  --cream:#f5f4f2;
  --white:#ffffff;
  --grey:#9a9a9a;
  --grey-light:#c9c9c9;
  --text-dark:#2b2b2b;
}
*{margin:0;padding:0;box-sizing:border-box}
html,body{width:756px;height:1200px;overflow:hidden}
body{position:relative;font-family:"Arimo",Arial,sans-serif;background:var(--brown)}
.site-backdrop{position:absolute;inset:0;background:radial-gradient(ellipse at 85% 40%,#d9a888 0%,#b07a58 30%,#5a3a2a 70%,#3a2519 100%)}
.page{position:absolute;left:53px;top:13px;width:648px;height:1174px;background:var(--cream);overflow:hidden}

/* header */
.site-header{height:74px;display:flex;align-items:center;justify-content:space-between;padding:0 14px;background:var(--white)}
.brand{display:flex;align-items:center;gap:10px}
.brand-mark{width:40px;height:40px;border-radius:50%;background:var(--taupe)}
.brand-name{font-family:"Questrial",sans-serif;font-size:22px;color:var(--brown-dark);white-space:nowrap}
.header-tools{display:flex;align-items:center;gap:8px}
.social{width:23px;height:23px;border-radius:50%;background:var(--grey-light)}
.search{display:flex;margin-left:14px}
.search-field{width:97px;height:23px;border:1px solid var(--teal);border-right:none;font-size:9px;color:var(--grey);padding:6px;background:var(--white)}
.search-btn{width:27px;height:23px;background:var(--teal);display:flex;align-items:center;justify-content:center}

/* nav */
.main-nav{height:30px;background:var(--brown-dark);display:flex;align-items:center;justify-content:space-between;padding-right:16px;overflow:hidden}
.main-nav a{flex:none;white-space:nowrap;color:#e9e2dc;font-size:9.5px;text-decoration:none;height:30px;line-height:30px}
.main-nav a.active{width:62px;text-align:center;background:var(--teal);color:var(--white)}

/* hero */
.hero-photo{height:243px;background:linear-gradient(120deg,#6b4a3a 0%,#c89478 35%,#e8c0a4 55%,#8a5a40 80%,#f0e9e3 100%)}
.hero-caption{height:114px;background:var(--teal);text-align:center;color:var(--white);padding-top:14px}
.hero-title{font-family:"Questrial",sans-serif;font-size:25px;font-weight:400;white-space:nowrap}
.hero-text{font-size:9px;line-height:14px;margin-top:8px}
.dots{display:flex;justify-content:center;gap:5px;margin-top:14px}
.dots span{width:9px;height:9px;border-radius:50%;background:var(--white)}
.dots span.current{background:#7fa9a7;border:2px solid var(--white)}

/* section titles */
.section-title{font-family:"Questrial",sans-serif;font-size:23px;font-weight:400;text-align:center;white-space:nowrap}
.title-rule{display:block;margin:6px auto 0}

/* services */
.services{height:314px;background:var(--cream);padding-top:22px}
.services .section-title{color:var(--text-dark)}
.service-list{display:flex;justify-content:space-between;padding:0 12px;margin-top:20px}
.service{width:144px;text-align:center}
.service-photo{width:112px;height:112px;border-radius:50%;border:5px solid var(--white);box-shadow:0 0 0 1px #ddd;margin:0 auto}
.service-name{font-family:"Questrial",sans-serif;font-size:15.5px;color:var(--teal);margin-top:11px;font-weight:400;white-space:nowrap}
.service-text{font-size:9px;line-height:11px;color:var(--grey-light);margin-top:4px;padding:0 4px}
.more-btn{display:inline-block;width:54px;height:24px;line-height:24px;background:var(--teal);color:var(--white);font-size:9px;margin-top:18px}

/* about */
.about{height:340px;background:linear-gradient(180deg,#3b2a22 0%,#2a1d17 60%,#3a2820 100%);padding-top:22px;position:relative}
.about .section-title{color:var(--white)}
.video-player{position:absolute;left:13px;top:79px;width:345px;height:233px;border:4px solid var(--white);background:#111}
.video-frame{height:198px;background:linear-gradient(135deg,#2a1a12 0%,#6b4a38 45%,#d9b8a0 75%,#c76f8c 100%)}
.video-controls{height:27px;display:flex;align-items:center;gap:10px;padding:0 8px;color:#ccc;font-size:8px;background:#1b1b1b;border-top:2px solid #555}
.about-text{position:absolute;left:385px;top:74px;width:252px;color:#f1ebe6;font-size:9.2px;line-height:14px}
.about-text p+p{margin-top:11px}

/* footer */
.site-footer{height:58px;background:var(--white);display:flex;align-items:center;font-size:9px;color:var(--grey);letter-spacing:.3px;white-space:nowrap}
.site-footer .left{width:320px;padding-left:102px}
.site-footer .divider{width:1px;height:34px;background:#ddd}
.site-footer .right{padding-left:38px}
</style>
</head>
<body>
<div class="site-backdrop" role="img" aria-label="Warm-toned spa photograph of a relaxing woman used as the page backdrop"></div>

<div class="page">
  <header class="site-header">
    <div class="brand">
      <span class="brand-mark"></span>
      <span class="brand-name">Verdant Spa</span>
    </div>
    <div class="header-tools">
      <span class="social"></span>
      <span class="social"></span>
      <span class="social"></span>
      <span class="social"></span>
      <div class="search">
        <span class="search-field">Search</span>
        <span class="search-btn">
          <svg width="11" height="11" viewBox="0 0 11 11"><circle cx="4.5" cy="4.5" r="3.2" fill="none" stroke="#fff" stroke-width="1.6"/><line x1="7" y1="7" x2="10" y2="10" stroke="#fff" stroke-width="1.8"/></svg>
        </span>
      </div>
    </div>
  </header>

  <nav class="main-nav">
    <a class="active">Home</a>
    <a>Price List</a>
    <a>Spa Services</a>
    <a>Bath and Body Products</a>
    <a>On Sale!</a>
    <a>The Goods On Our Services</a>
    <a>Jobs Listing</a>
  </nav>

  <div class="hero-photo" role="img" aria-label="Woman receiving a back massage on a spa table with flowers and candles"></div>
  <section class="hero-caption">
    <h1 class="hero-title">Welcome to Verdant Spa</h1>
    <p class="hero-text">Verdant Spa is a full service day spa with registered massage therapists, comprehensive esthetical services,<br>and our own exclusive line of custom hand made bath and body products.</p>
    <div class="dots"><span></span><span class="current"></span><span></span></div>
  </section>

  <section class="services">
    <h2 class="section-title">Our Services</h2>
    <svg class="title-rule" width="264" height="8" viewBox="0 0 264 8"><line x1="0" y1="4" x2="264" y2="4" stroke="#333" stroke-width="1"/><circle cx="126" cy="4" r="2" fill="#333"/><circle cx="138" cy="4" r="2" fill="#333"/></svg>
    <div class="service-list">
      <div class="service">
        <div class="service-photo" role="img" aria-label="Close-up of hands receiving a manicure" style="background:radial-gradient(circle,#f3d6c8,#d9a58f)"></div>
        <h3 class="service-name">Perhaps manicures</h3>
        <p class="service-text">Lorem ipsum dolor sit amet, consectetuer adipiscing elit, sed diam nonummy nibh euismod.</p>
        <span class="more-btn">More</span>
      </div>
      <div class="service">
        <div class="service-photo" role="img" aria-label="Feet with a pink flower during a pedicure" style="background:radial-gradient(circle,#f5ddd0,#e0b09c)"></div>
        <h3 class="service-name">Pedicures</h3>
        <p class="service-text">Lorem ipsum dolor sit amet, consectetuer adipiscing elit, sed diam nonummy nibh euismod.</p>
        <span class="more-btn">More</span>
      </div>
      <div class="service">
        <div class="service-photo" role="img" aria-label="Woman lying down during a hot stone massage" style="background:radial-gradient(circle,#b07050,#3a2016)"></div>
        <h3 class="service-name">Massage</h3>
        <p class="service-text">Lorem ipsum dolor sit amet, consectetuer adipiscing elit, sed diam nonummy nibh euismod.</p>
        <span class="more-btn">More</span>
      </div>
      <div class="service">
        <div class="service-photo" role="img" aria-label="Fingernails painted with pink gel nail art" style="background:radial-gradient(circle,#f6e3e6,#d99aa8)"></div>
        <h3 class="service-name">Gel Nails</h3>
        <p class="service-text">Lorem ipsum dolor sit amet, consectetuer adipiscing elit, sed diam nonummy nibh euismod.</p>
        <span class="more-btn">More</span>
      </div>
    </div>
  </section>

  <section class="about">
    <h2 class="section-title">About Video</h2>
    <svg class="title-rule" width="264" height="8" viewBox="0 0 264 8"><line x1="0" y1="4" x2="264" y2="4" stroke="#ddd" stroke-width="1"/><circle cx="126" cy="4" r="2" fill="#fff"/><circle cx="138" cy="4" r="2" fill="#fff"/></svg>

    <div class="video-player">
      <div class="video-frame" role="img" aria-label="Video still of a woman relaxing beside candles and lotus flowers"></div>
      <div class="video-controls">
        <svg width="9" height="10" viewBox="0 0 9 10"><polygon points="0,0 9,5 0,10" fill="#ccc"/></svg>
        <svg width="11" height="10" viewBox="0 0 11 10"><polygon points="0,3 3,3 6,0 6,10 3,7 0,7" fill="#ccc"/><path d="M8 2 Q11 5 8 8" stroke="#ccc" fill="none"/></svg>
        <span>0:00 / 0:29</span>
      </div>
    </div>

    <div class="about-text">
      <p>Verdant spa is a full service day spa with a staff of experienced registered massage therapists and estheticians. We perform therapeutic massage, hot or cold stone massage, or just relaxation.</p>
      <p>We do pedicures, manicures, gel nails, waxing, threading, artificial eyelash extensions and more. Our services offer an optional selection of scented products at no extra charge, and we change the scents monthly for a variety that nobody else can match. We offer a selection of spa packages for you, or someone you care about, or make your own package.</p>
      <p>We carry our exclusive line of bath and body products, all made from select natural ingredients. You won't find any mineral oils or parabens in our products, and we never test on animals. You can choose from our selection of over 75 types of products on the shelf, or have your product custom made in any of our 120 different scents while you wait.</p>
    </div>
  </section>

  <footer class="site-footer">
    <span class="left">VERDANT SPA © 2014 &nbsp;/&nbsp; ALL RESERVED</span>
    <span class="divider"></span>
    <span class="right">DESIGNED &amp; DEVELOPED BY LOOMCRAFT STUDIO</span>
  </footer>
</div>
</body>
</html>
```